PowerPoint Design Project

Hi,

Using our logo, we would like a designer to provide us with a powerpoint template that has a unique brand.

To us this means creating a color palette, treatment, a font that plays off of our logo. The color palette needs to blend well with our existing colors, but give us some options, make things "POP".

The color palette needs to include the colors (with RGB numbers), gradients, different graphic styles (solid, transparent, gradient, image fills) and lines (a callout leader line, a multi-color bar to divide content)

The palette and treatment must extend itself to graphs, charts and images.

We would also like to see different parts of our logo applied to the different template slides. For example, on a title slide we would like the image with our logo and tagline. With the end slide we would like to see our logo and URL. We also attached our logo without the tagline and also just the colored cube. So please be creative on how these are incorporated into the deck.

Images are attached.

Thank you
Carlton

Target Market(s)

Large Corporations

Requirements
Must have
• color palette, treatments and consistent fonts. color palette must complement our logo. color palette must extend to graphs, charts and images.

different logo's incorprated into the deck. For example, on a title slide we would like the image with our logo and tagline. With the end slide we would like to see our logo and URL. We also attached our logo without the tagline and also just the colored cube. So please be creative on how these are incorporated into the deck.
Should not have
• We do not want to see designers taking the logo and incorporating them into the background and calling it a template.

```html
<!DOCTYPE html>
<html lang="en">
<head>
<meta charset="utf-8">
<title>vantrelgroup presentation template</title>
<link rel="stylesheet" href="https://fonts.googleapis.com/css2?family=Alegreya+Sans:wght@400;500;700&family=Open+Sans:wght@400;600&display=swap">
<style>
:root{
  --stage:#b4b6be;
  --paper-top:#ffffff;
  --paper-bottom:#e3e5ee;
  --teal:#2ba4c1;
  --teal-bar:#3fb3c9;
  --sky:#58c3f0;
  --ocean-top:#3cb0c9;
  --ocean-bottom:#1664a9;
  --green:#7fbb3a;
  --ink:#2a2a2e;
  --body:#3b3d44;
  --rule:#c9cdd8;
  --cell:#d6dae3;
  --footer-top:#41454f;
  --footer-bottom:#23262d;
  --brand-blue:#1f5fae;
  --faint:#c4c8d2;
}
*{margin:0;padding:0;box-sizing:border-box}
html,body{width:1200px;height:909px;overflow:hidden}
body{background:var(--stage);position:relative;font-family:"Open Sans",Arial,sans-serif}
.slide{position:absolute;width:582px;height:436px;overflow:hidden;background:linear-gradient(180deg,var(--paper-top),var(--paper-bottom))}
.slide--title{left:14px;top:10px}
.slide--section{left:605px;top:10px;background:linear-gradient(180deg,var(--ocean-top),var(--ocean-bottom))}
.slide--content{left:14px;top:457px}
.slide--table{left:605px;top:457px}

/* title slide */
.title-brand{position:absolute;left:130px;top:182px;display:flex;align-items:center;gap:16px}
.brand-square{width:48px;height:48px;background:var(--brand-blue)}
.title-name{font-family:"Alegreya Sans",Arial,sans-serif;font-weight:500;font-size:50px;line-height:1;color:var(--ink);letter-spacing:-0.5px}
.title-tagline{position:absolute;left:198px;top:246px;font-family:"Open Sans",Arial,sans-serif;font-size:11px;letter-spacing:2px;text-transform:uppercase;color:var(--teal)}

/* section slide */
.section-head{position:absolute;left:96px;top:175px;display:flex;align-items:center;gap:20px}
.section-square{width:62px;height:62px;background:var(--sky);opacity:.9}
.section-word{font-family:"Alegreya Sans",Arial,sans-serif;font-weight:500;font-size:66px;line-height:1;color:var(--sky)}

/* shared content chrome */
.top-bar{position:absolute;left:0;top:0;width:100%;height:4px;background:var(--teal-bar)}
.slide-title{position:absolute;left:6px;top:12px;font-family:"Alegreya Sans",Arial,sans-serif;font-weight:500;font-size:21px;line-height:24px;color:var(--teal)}
.title-rule{position:absolute;left:0;top:38px;width:282px;height:1px;background:var(--rule)}
.header-brand{position:absolute;left:300px;top:27px;display:flex;align-items:center;gap:6px}
.header-square{width:14px;height:14px;background:var(--faint)}
.header-name{font-family:"Alegreya Sans",Arial,sans-serif;font-weight:500;font-size:19px;line-height:20px;color:var(--faint)}
.footer{position:absolute;left:0;bottom:0;width:100%;height:43px;background:linear-gradient(180deg,var(--footer-top),var(--footer-bottom))}
.page-number{position:absolute;left:14px;top:16px;font-size:9px;color:var(--teal)}
.footer-mail{position:absolute;right:316px;top:15px;font-size:9px;color:var(--teal)}
.footer-square{position:absolute;left:281px;top:12px;width:18px;height:18px;background:var(--teal)}
.footer-web{position:absolute;left:311px;top:15px;font-size:9px;color:var(--teal)}

/* content slide */
.portrait{position:absolute;left:34px;top:48px;width:197px;height:345px;background:linear-gradient(180deg,#d8dbe2 0%,#2d3444 40%,#1c2230 100%)}
.points{position:absolute;left:256px;top:80px;width:300px}
.point-heading{font-family:"Alegreya Sans",Arial,sans-serif;font-size:12.5px;line-height:15px;color:var(--teal);margin-left:25px;margin-bottom:1px}
.point{position:relative;padding-left:25px;font-size:8.6px;line-height:12.5px;color:var(--body);margin-bottom:13px}
.point::before{content:"";position:absolute;left:0;top:3px;width:9px;height:9px;background:var(--teal)}
.points-divider{height:1px;background:var(--rule);margin:10px 0 18px 20px;width:278px}

/* table slide */
.quarter-table{position:absolute;left:49px;top:99px;width:481px;border-collapse:collapse;table-layout:fixed;font-family:"Alegreya Sans",Arial,sans-serif}
.quarter-table th{width:25%;height:36px;background:linear-gradient(180deg,#4a4f5b,#2f333c);color:var(--teal);font-size:14px;font-weight:700;border-right:1px solid #5b606c}
.quarter-table th.is-green,.quarter-table td.is-green{color:var(--green)}
.quarter-table td{height:39px;border:1px solid var(--cell);font-family:"Open Sans",Arial,sans-serif;font-size:8.5px;color:var(--teal);text-align:center}
.quarter-table tr.label-row td{background:rgba(255,255,255,.55)}
</style>
</head>
<body>

<section class="slide slide--title">
  <div class="title-brand">
    <div class="brand-square"></div>
    <div class="title-name">vantrelgroup</div>
  </div>
  <div class="title-tagline">clarity . growth . change</div>
</section>

<section class="slide slide--section">
  <div class="section-head">
    <div class="section-square"></div>
    <div class="section-word">analyze</div>
  </div>
</section>

<section class="slide slide--content">
  <div class="top-bar"></div>
  <h2 class="slide-title">analyze</h2>
  <div class="title-rule"></div>
  <div class="header-brand"><div class="header-square"></div><span class="header-name">vantrelgroup</span></div>
  <div class="portrait" role="img" aria-label="Photo of a businessman in a dark suit and tie, hands folded"></div>
  <div class="points">
    <div class="point-heading">Analyze</div>
    <p class="point">Aenean ridiculus tortor quis interdum id habitant ad, natoque consectetuer nisl auctor libero quisque euismod ante inceptos malesuada ligula mattis.</p>
    <p class="point">Nulla, netus pulvinar pellentesque porttitor purus maecenas tellus hac nulla lacus. Lorem. Nostra laoreet nulla, dis cursus nascetur dolor odio Eu Magna molestie montes dui mus cursus habitasse mauris tempor.</p>
    <p class="point">Varius inceptos nascetur mollis dui aptent ultrices. Pretium pulvinar ante lobortis convallis lectus netus vitae penatibus eros at blandit. Parturient.</p>
    <div class="points-divider"></div>
    <div class="point-heading">Elevate</div>
    <p class="point">Aenean ridiculus tortor quis interdum id habitant ad, natoque consectetuer nisl auctor libero quisque euismod ante inceptos malesuada ligula mattis.</p>
    <p class="point">Nulla, netus pulvinar pellentesque porttitor purus maecenas tellus hac nulla lacus. Lorem. Nostra laoreet nulla, dis cursus nascetur dolor odio</p>
  </div>
  <footer class="footer">
    <span class="page-number">3</span>
    <span class="footer-mail">info@vantrelgroup.com</span>
    <span class="footer-square"></span>
    <span class="footer-web">www.vantrelgroup.com</span>
  </footer>
</section>

<section class="slide slide--table">
  <div class="top-bar"></div>
  <h2 class="slide-title">table</h2>
  <div class="title-rule"></div>
  <div class="header-brand"><div class="header-square"></div><span class="header-name">vantrelgroup</span></div>
  <table class="quarter-table">
    <tr><th>1Q</th><th>2Q</th><th class="is-green">3Q</th><th>4Q</th></tr>
    <tr class="label-row"><td>Text</td><td>Figures</td><td class="is-green">Amounts</td><td>Results</td></tr>
    <tr><td></td><td></td><td></td><td></td></tr>
    <tr><td></td><td></td><td></td><td></td></tr>
    <tr><td></td><td></td><td></td><td></td></tr>
    <tr><td></td><td></td><td></td><td></td></tr>
    <tr><td></td><td></td><td></td><td></td></tr>
  </table>
  <footer class="footer">
    <span class="page-number">4</span>
    <span class="footer-mail">info@vantrelgroup.com</span>
    <span class="footer-square"></span>
    <span class="footer-web">www.vantrelgroup.com</span>
  </footer>
</section>

</body>
</html>
```